Mockup design for a fashion contest website

The website is a landing page for a fashion contest. Participants are fashion students, designers, merchandisers, stylists, and other fashion enthusiasts. Website should have a clean, modern look and should be "headline-y" in nature. Website should be very visual with good use of images since the audience is fashion (specifically women's clothing). Contestants will earn points by identifying fashion/clothing items within images.

Here's what I am thinking:

Title:
Fashion Contest by Vendrow

Headlines (each with subheadline of 10-15 words )
Can you find the features in the image?
This will be a carousel showing 3-4 images with callouts
Have callouts for each of the categories like this: https://img.qorvexa.example/v/7TmWq2LpZr/fullview.jpg
Broad categories for items are labeled like:
Top
Dress
Jeans
Pants
Shorts
Blouse
Skirt
Standard
Crop Top
Shirt
Sweater
Detail fashion attributes are in the spreadsheet attached

Earn Points
and see where you stand -- leaderboard graphic
Win Prizes
Need a way to show multiple prizes here:
Grand prizes: Tablo Max, Kelvar Snapline KZ-TR720Q Wi-Fi Digital Camera, Halden QM480TXV Sewing Machine, Drevo Linemark Plus Drawing tablet
Other prizes: Noral Earlets, Gift cards to great stores: Vimo, Keto, Lumirel, etc.

What You Need To Know
How to Enter (25-30 words)
How do I qualify? (10-15 words)
What are the contest dates (10-15 words)
What is this for? (10-15 words)

----

Tell Your Friends (10 words) [Needs to be shown more prominently as we will have referral bonuses]

The Legal Stuff / Terms & Conditions
[Each subsection 50 words]
Eligibility
Winners & Prizes
Privacy Policy
Judging
Disclaimer

Other sections (shown as links on top perhaps)
Blog - standard blog format. No need for design
Forum - use threadhall software. No need for design
Standings
FAQ
Contact - link to email - no need for design

Need to have clear CTA to sign up on bottom.

Need to Design ‘Standings’ Page:

Show Leaderboard
Ranking, Username, total points, change in ranking (up or down)

Show Total number of images processed. This can be progress bar like in crowdfunding sites:
https://snapdrop.example/kWtrb/91ab3d6f27.png
It would say:
300,000 images processed by 1,000 participants
x% of 1,000,000 goal a month left

Goals and Stretch Goals for the Contest

500,000 images
Grand prizes (1 winner)
Other prizes (3 winners)

1,000,000 images
Grand prizes (2 winners)
Other prizes (6 winners)

2,000,000 images
Grand prizes (3 winners)
Other prizes (9 winners)

3,000,000 images
Grand prizes (4 winners)
Other prizes (12 winners)

How to Earn Points

Points awarded for correctly completing task
Points are deducted for making mistakes and unnecessary skips

Help
just a click away. Post a message on the community forum and ask a question.
----
High contrasty (black & white) with one color perhaps blue should be color palette. Look at our logo for design motif ideas.

Welcome to the contest. I will be guaranteeing the project once at least one usable design comes in. Good luck to all! Added Tuesday, March 14, 2017

Target Market(s)

Fashion community

Industry/Entity Type

Fashion

Number of Pages Required

2 page

Font styles to use
Sans Serif

Requirements
Must have
• one page scroll website (the quiz is a separate page though)
• beautiful graphics and images
• placeholder text where number of words is written
Nice to have
• written copy ideas
Should not have
• the vendrow logo should not be prominently featured. the emphasis is on 'Fashion Contest'

```html
<!DOCTYPE html>
<html lang="en">
<head>
<meta charset="utf-8">
<title>Fashion Contest by Vendrow</title>
<link rel="stylesheet" href="https://fonts.googleapis.com/css2?family=Raleway:wght@400;500;600;700&family=Roboto+Slab:wght@400;500;700&display=swap">
<style>
:root{
  --navy:#0f1b52;
  --navy-deep:#0a1340;
  --navy-soft:#1d2b6e;
  --ink:#1b1b1f;
  --muted:#55586a;
  --line:#d7d9e2;
  --paper:#ffffff;
  --mist:#f3f4f7;
  --violet:#8a3fd1;
  --indigo:#3a3fb8;
}
*{box-sizing:border-box;margin:0;padding:0}
html,body{width:1200px;height:3455px;overflow:hidden}
body{font-family:"Raleway",Arial,sans-serif;color:var(--ink);background:var(--paper);position:relative}
.photo{display:block}
.section-title{font-family:"Roboto Slab",Georgia,serif;font-weight:400;font-size:30px;color:var(--navy);text-align:center}
.section-sub{font-size:12.5px;color:var(--ink);text-align:center;margin-top:8px}

/* header */
.site-header{position:absolute;top:0;left:0;width:1200px;height:62px;background:var(--paper);z-index:3}
.brand{position:absolute;left:98px;top:12px;display:flex;align-items:center;gap:10px}
.brand-mark{width:26px;height:26px;background:var(--navy)}
.brand-name{font-family:"Roboto Slab",Georgia,serif;font-size:33px;font-weight:400;color:var(--navy);letter-spacing:1px}
.main-nav{position:absolute;left:594px;top:12px;height:40px;width:392px;background:var(--navy);border-radius:20px 0 0 20px;display:flex;align-items:center;padding-left:22px;gap:2px;white-space:nowrap}
.main-nav a{color:#fff;text-decoration:none;font-size:12px;padding:6px 9px}
.main-nav a.active{background:var(--navy-soft);border-radius:3px}
.social{position:absolute;left:990px;top:12px;display:flex;gap:4px}
.social span{width:30px;height:40px;background:var(--navy);display:flex;align-items:center;justify-content:center}
.social span i{width:11px;height:11px;background:#fff;display:block}
.search-btn{width:30px;height:40px;background:var(--navy);display:flex;align-items:center;justify-content:center}
.header-rule{position:absolute;left:1126px;top:12px;width:74px;height:40px;border-top:2px solid var(--navy);border-bottom:2px solid var(--navy)}

/* hero */
.hero{position:absolute;top:62px;left:0;width:1200px;height:620px;border-bottom:4px solid var(--navy)}
.hero .photo{width:100%;height:100%;background:linear-gradient(90deg,#5a3a34 0%,#b87a66 18%,#e8d2c8 38%,#f4eef0 60%,#e9e6ee 100%)}
.hero-copy{position:absolute;left:677px;top:226px;width:440px}
.hero-title{font-family:"Roboto Slab",Georgia,serif;font-size:32px;font-weight:400;color:var(--navy);padding-bottom:10px;border-bottom:1px dashed var(--navy);width:420px}
.hero-copy p{font-size:11.5px;line-height:18px;margin-top:12px;color:var(--ink)}
.btn{display:inline-block;background:var(--navy);color:#fff;text-decoration:none;border-radius:24px;font-size:17px}
.hero .btn{margin-top:18px;padding:12px 46px}
.dots{position:absolute;left:1062px;top:586px;display:flex;gap:3px}
.dots i{width:11px;height:11px;border:2px solid var(--navy);border-radius:50%;display:block}
.dots i.on{background:var(--navy)}

/* features */
.features{position:absolute;top:686px;left:0;width:1200px;height:551px}
.features .section-title{margin-top:24px}
.categories{position:absolute;left:99px;top:122px;width:267px;border:1px solid var(--line)}
.categories header{background:var(--navy);color:#fff;text-align:center;padding:6px 0 7px}
.categories header h3{font-family:"Roboto Slab",Georgia,serif;font-weight:400;font-size:20px}
.categories header p{font-size:10.5px;margin-top:2px}
.categories ul{list-style:none}
.categories li{font-size:12.5px;height:31px;line-height:31px;padding-left:12px;border-top:1px solid var(--line)}
.categories li.active{background:var(--navy);color:#fff}
.showcase{position:absolute;left:389px;top:122px;width:712px;height:293px;border:2px solid var(--navy)}
.showcase .photo{width:100%;height:100%;background:linear-gradient(100deg,#2a2a30 0%,#8a8d94 30%,#5d7aa6 55%,#c9d3e2 75%,#e9e9ec 100%)}
.caption{position:absolute;left:0;top:166px;width:302px;height:54px;background:var(--navy);color:#fff;padding:7px 14px}
.caption small{font-size:10.5px;display:block}
.caption strong{font-family:"Roboto Slab",Georgia,serif;font-weight:400;font-size:18px;letter-spacing:.5px}
.arrows{position:absolute;left:313px;top:260px;display:flex}
.arrows span{width:40px;height:33px;background:var(--navy);display:flex;align-items:center;justify-content:center}
.thumbs{position:absolute;left:389px;top:426px;width:712px;display:flex;gap:12px}
.thumbs .photo{width:229px;height:97px;border:1px solid var(--line)}
.thumbs .t1{background:linear-gradient(90deg,#c8c9cc,#3a3633 50%,#b9b9bd)}
.thumbs .t2{background:linear-gradient(90deg,#8d8a86,#4b5f7c 50%,#d7d3cf)}
.thumbs .t3{background:linear-gradient(90deg,#e4e4e7,#1d1d22 45%,#c5c7cc);border:3px solid var(--navy)}

/* leaderboard */
.points{position:absolute;top:1237px;left:0;width:1200px;height:354px;background:radial-gradient(ellipse at 20% 40%,#e4e4e6 0%,#f5f5f6 40%,#ffffff 70%),#fafafa}
.points .section-title{margin-top:24px}
.points .section-sub{margin-top:5px;font-size:11.5px}
.board{position:absolute;left:279px;top:104px;width:707px;list-style:none}
.board li{position:relative;height:30px;margin-bottom:4px;background:linear-gradient(115deg,var(--navy) 0%,var(--navy) 62%,#5c6690 62.2%,#8a91ad 100%);border-radius:3px;color:#fff;font-size:12px;display:flex;align-items:center;padding:0 10px;overflow:hidden}
.board .name{width:315px}
.board .stars{letter-spacing:1px;font-size:13px}
.board .pct{position:absolute;right:14px;color:#fff;font-size:11.5px}

/* prizes */
.prizes{position:absolute;top:1591px;left:0;width:1200px;height:429px;background:linear-gradient(90deg,var(--violet) 0%,#5b36b8 35%,var(--indigo) 60%,#1d2f8d 100%)}
.prizes .section-title{color:#fff;margin-top:40px}
.prizes .section-sub{color:#fff;font-size:11.5px;margin-top:6px}
.prize-list{position:absolute;left:101px;top:136px;list-style:none}
.prize{display:flex;width:477px;height:78px;margin-bottom:9px}
.prize .body{flex:1;background:#fff;padding:9px 10px;border-radius:3px 0 0 3px}
.prize h3{font-family:"Roboto Slab",Georgia,serif;font-weight:400;font-size:18px;color:var(--navy)}
.prize p{font-size:11px;line-height:15px;margin-top:3px;color:var(--muted)}
.prize .icon{width:78px;background:var(--navy);display:flex;align-items:center;justify-content:center}
.gift-art{position:absolute;left:790px;top:130px;width:320px;height:250px;background:radial-gradient(circle at 55% 55%,rgba(255,255,255,.28) 0%,rgba(255,255,255,.08) 45%,rgba(255,255,255,0) 70%)}

/* info */
.info{position:absolute;top:2020px;left:0;width:1200px;height:301px}
.info .section-title{margin-top:38px}
.info .section-sub{font-size:11.5px;margin-top:6px}
.info-grid{position:absolute;left:90px;top:148px;width:1020px;display:flex}
.info-item{flex:1;text-align:center}
.info-item svg{height:44px}
.info-item h3{font-size:15px;font-weight:500;margin-top:10px}
.info-item p{font-size:11px;line-height:15px;color:var(--muted);margin:4px auto 0;width:210px}

/* share */
.share{position:absolute;top:2321px;left:0;width:1200px;height:224px;background:var(--navy-deep)}
.share .photo{position:absolute;left:530px;top:0;width:670px;height:224px;background:linear-gradient(90deg,var(--navy-deep) 0%,#3b3550 25%,#8a6f66 50%,#a88a7a 70%,#6a5a58 100%)}
.share-pill{position:absolute;left:0;top:79px;width:426px;height:64px;border:2px solid #fff;border-left:none;border-radius:0 32px 32px 0;padding:8px 0 0 98px;color:#fff}
.share-pill h2{font-family:"Roboto Slab",Georgia,serif;font-weight:400;font-size:27px}
.share-pill p{font-size:11.5px;margin-top:2px}
.share-pill svg{position:absolute;right:-16px;top:20px;background:var(--navy-deep)}

/* legal */
.legal{position:absolute;top:2545px;left:0;width:1200px;height:345px}
.legal .photo{position:absolute;inset:0;background:linear-gradient(90deg,#6a5e58 0%,#2a2526 20%,#a59a96 38%,#d9d7d8 52%,#ececee 62%,#efeff1 100%)}
.legal-copy{position:absolute;left:663px;top:42px;width:470px}
.legal-copy h2{font-family:"Roboto Slab",Georgia,serif;font-weight:400;font-size:23px;color:var(--navy)}
.legal-copy ul{list-style:none;margin-top:12px;padding-left:18px}
.legal-copy li{margin-bottom:5px}
.legal-copy h3{font-size:13.5px;font-weight:700;color:var(--navy);display:flex;align-items:center;gap:6px;margin-left:-18px}
.legal-copy p{font-size:11.5px;margin-top:3px;color:var(--ink)}

/* blog */
.blog{position:absolute;top:2890px;left:0;width:1200px;height:514px}
.blog .section-title{margin-top:30px}
.blog .section-sub{font-size:11.5px;margin-top:6px}
.posts{position:absolute;left:145px;top:111px;display:flex;gap:40px}
.post{width:272px;height:366px;background:#fff;box-shadow:0 0 8px rgba(0,0,0,.16)}
.post .photo{height:127px}
.post .p1{background:linear-gradient(90deg,#e8e2de,#b68a6e 50%,#f0ece8)}
.post .p2{background:linear-gradient(90deg,#c2b8b0,#3d3532 55%,#d9d2cb)}
.post .p3{background:linear-gradient(90deg,#a6a8ab,#e3e4e6 40%,#2c2c30 60%,#cfd0d3)}
.post .body{padding:12px 12px 0}
.post h3{font-family:"Roboto Slab",Georgia,serif;font-weight:400;font-size:17px}
.post time{display:block;font-size:8.5px;text-align:center;margin-top:1px;width:110px}
.post p{font-size:11.5px;line-height:17px;margin-top:8px}
.post .btn{font-size:14px;padding:8px 36px;margin-top:14px}

/* footer */
.site-footer{position:absolute;top:3400px;left:0;width:1200px;height:55px;border-top:2px solid var(--navy)}
.site-footer small{position:absolute;left:99px;top:28px;font-size:10.5px}
.footer-nav{position:absolute;right:90px;top:26px;display:flex;gap:26px}
.footer-nav a{font-size:11px;color:var(--ink);text-decoration:none}
.signup{position:absolute;left:511px;top:-20px;width:176px;height:44px;line-height:44px;text-align:center;padding:0;font-size:19px}
</style>
</head>
<body>

<header class="site-header">
  <div class="brand"><span class="brand-mark"></span><span class="brand-name">VENDROW</span></div>
  <nav class="main-nav">
    <a class="active" href="#">Home</a><a href="#">Forum</a><a href="#">Standings</a><a href="#">FAQ</a><a href="#">Blog</a><a href="#">Contact</a>
  </nav>
  <div class="social">
    <span><i></i></span><span><i></i></span><span><i></i></span>
    <span class="search-btn"><svg width="15" height="15" viewBox="0 0 16 16"><circle cx="6.5" cy="6.5" r="5" fill="none" stroke="#fff" stroke-width="2"/><line x1="10.3" y1="10.3" x2="15" y2="15" stroke="#fff" stroke-width="2.4"/></svg></span>
  </div>
  <div class="header-rule"></div>
</header>

<section class="hero">
  <div class="photo" role="img" aria-label="Smiling young woman in round sunglasses, flower crown and white crochet top"></div>
  <div class="hero-copy">
    <h1 class="hero-title">Fashion Contest by Vendrow</h1>
    <p>Lorem Ipsum is simply dummy text of the printing and typesetting industry<br>Lorem Ipsum has been the industry's standard dummy</p>
    <a class="btn" href="#">Apply Now</a>
  </div>
  <div class="dots"><i></i><i class="on"></i><i></i></div>
</section>

<section class="features">
  <h2 class="section-title">Fashion Contest by Vendrow</h2>
  <p class="section-sub">Lorem Ipsum is simply dummy text of the printing and typesetting industry</p>
  <aside class="categories">
    <header><h3>Categories</h3><p>Broad categories for items are labeled like:</p></header>
    <ul>
      <li>Top</li><li>Dress</li><li class="active">Jeans</li><li>Pants</li><li>Shorts</li><li>Blouse</li><li>Skirt</li><li>Standard</li><li>Crop Top</li><li>Shirt</li><li>Sweater</li>
    </ul>
  </aside>
  <div class="showcase">
    <div class="photo" role="img" aria-label="Close view of ripped blue jeans with a black leather jacket"></div>
    <div class="caption"><small>Design by</small><strong>Sela Marwood</strong></div>
    <div class="arrows">
      <span><svg width="10" height="12" viewBox="0 0 10 12"><path d="M8 1 2 6l6 5" fill="none" stroke="#fff" stroke-width="2"/></svg></span>
      <span><svg width="10" height="12" viewBox="0 0 10 12"><path d="M2 1l6 5-6 5" fill="none" stroke="#fff" stroke-width="2"/></svg></span>
    </div>
  </div>
  <div class="thumbs">
    <div class="photo t1" role="img" aria-label="Woman in dark coat holding a handbag"></div>
    <div class="photo t2" role="img" aria-label="Denim jeans with a brown belt"></div>
    <div class="photo t3" role="img" aria-label="Woman in black outfit walking"></div>
  </div>
</section>

<section class="points">
  <h2 class="section-title">Earn Points</h2>
  <p class="section-sub">Lorem Ipsum is simply dummy text of the printing</p>
  <ol class="board">
    <li><span class="name">Joren Altava</span><span class="stars">★★★★½</span><span class="pct">90%</span></li>
    <li><span class="name">Adela Anvre</span><span class="stars">★★★★</span><span class="pct">80%</span></li>
    <li><span class="name">Pierrot Balmont</span><span class="stars">★★★½</span><span class="pct">75%</span></li>
    <li><span class="name">Piet Cardell</span><span class="stars">★★★</span><span class="pct">60%</span></li>
    <li><span class="name">Cora Chaval</span><span class="stars">★★★</span><span class="pct">61%</span></li>
    <li><span class="name">Louisa Cherel</span><span class="stars">★★½</span><span class="pct">59%</span></li>
  </ol>
</section>

<section class="prizes">
  <h2 class="section-title">Win Prizes</h2>
  <p class="section-sub">Lorem Ipsum is simply dummy text of the</p>
  <ul class="prize-list">
    <li class="prize"><div class="body"><h3>Grand prizes</h3><p>Tablo Max, Kelvar Snapline KZ-TR720Q Wi-Fi Digital Camera, Halden QM480TXV Sewing Machine, Drevo Linemark Plus Drawing tablet</p></div>
      <div class="icon"><svg width="34" height="34" viewBox="0 0 34 34" fill="none" stroke="#fff" stroke-width="2"><rect x="4" y="12" width="26" height="7"/><rect x="6" y="19" width="22" height="12"/><line x1="17" y1="12" x2="17" y2="31"/><path d="M17 12c-3-6-9-6-8-2s8 2 8 2c3-6 9-6 8-2s-8 2-8 2"/></svg></div></li>
    <li class="prize"><div class="body"><h3>Winner prizes</h3><p>Tablo Max, Kelvar Snapline KZ-TR720Q Wi-Fi Digital Camera, Halden QM480TXV Sewing Machine, Drevo Linemark Plus Drawing tablet</p></div>
      <div class="icon"><svg width="34" height="34" viewBox="0 0 34 34" fill="none" stroke="#fff" stroke-width="2"><rect x="4" y="12" width="26" height="7"/><rect x="6" y="19" width="22" height="12"/><line x1="17" y1="12" x2="17" y2="31"/><path d="M17 12c-3-6-9-6-8-2s8 2 8 2c3-6 9-6 8-2s-8 2-8 2"/></svg></div></li>
    <li class="prize"><div class="body"><h3>Other prizes</h3><p>Tablo Max, Kelvar Snapline KZ-TR720Q Wi-Fi Digital Camera, Halden QM480TXV Sewing Machine, Drevo Linemark Plus Drawing tablet</p></div>
      <div class="icon"><svg width="34" height="34" viewBox="0 0 34 34" fill="none" stroke="#fff" stroke-width="2"><rect x="4" y="12" width="26" height="7"/><rect x="6" y="19" width="22" height="12"/><line x1="17" y1="12" x2="17" y2="31"/><path d="M17 12c-3-6-9-6-8-2s8 2 8 2c3-6 9-6 8-2s-8 2-8 2"/></svg></div></li>
  </ul>
  <div class="gift-art" role="img" aria-label="Line illustration of an open gift box with stars bursting out, surrounded by small faint gift boxes"></div>
</section>

<section class="info">
  <h2 class="section-title">What You Need To Know</h2>
  <p class="section-sub">Lorem Ipsum is simply dummy text of the printing and typesetting</p>
  <div class="info-grid">
    <div class="info-item">
      <svg viewBox="0 0 44 44" width="44" fill="none" stroke="var(--navy)" stroke-width="2"><path d="M16 6h18v32H16"/><path d="M16 6v6M16 32v6"/><path d="M6 22h18M19 17l5 5-5 5"/></svg>
      <h3>How to Enter</h3><p>Lorem Ipsum is simply dummy text of the printing and</p></div>
    <div class="info-item">
      <svg viewBox="0 0 44 44" width="44" fill="none" stroke="var(--navy)" stroke-width="2"><path d="M11 5h16l7 7v27H11z"/><path d="M27 5v7h7"/><path d="M16 20h13M16 25h13M16 30h13"/></svg>
      <h3>How do I qualify?</h3><p>Lorem Ipsum is simply dummy text of the printing and</p></div>
    <div class="info-item">
      <svg viewBox="0 0 44 44" width="44" fill="none" stroke="var(--navy)" stroke-width="2"><rect x="6" y="8" width="32" height="30"/><path d="M6 15h32M14 4v7M30 4v7"/><text x="22" y="33" text-anchor="middle" font-family="Raleway,sans-serif" font-size="14" fill="var(--navy)" stroke="none" font-weight="600">19</text></svg>
      <h3>What are the contest dates</h3><p>Lorem Ipsum is simply dummy text of the printing and</p></div>
    <div class="info-item">
      <svg viewBox="0 0 44 44" width="44" fill="none" stroke="var(--navy)" stroke-width="3"><path d="M16 15a6 6 0 1 1 9 5c-2 1-3 2-3 5v2"/><circle cx="22" cy="33" r="1.5" fill="var(--navy)"/></svg>
      <h3>What is this for</h3><p>Lorem Ipsum is simply dummy text of the printing and</p></div>
  </div>
</section>

<section class="share">
  <div class="photo" role="img" aria-label="Row of models in sequined dresses on a runway"></div>
  <div class="share-pill">
    <h2>Tell Your Friends</h2>
    <p>Lorem Ipsum is simply dummy text of the printing</p>
    <svg width="30" height="22" viewBox="0 0 30 22" fill="none" stroke="#fff" stroke-width="1.8"><rect x="2" y="2" width="26" height="18"/><path d="M2 2l13 10L28 2"/></svg>
  </div>
</section>

<section class="legal">
  <div class="photo" role="img" aria-label="Two women in sunglasses and black outfits at a street fashion event"></div>
  <div class="legal-copy">
    <h2>The Legal Stuff / Terms &amp; Conditions</h2>
    <ul>
      <li><h3><svg width="12" height="12" viewBox="0 0 12 12"><rect x=".5" y=".5" width="11" height="11" fill="none" stroke="var(--navy)"/><path d="M2.5 6l2.5 2.5 5-6" fill="none" stroke="var(--navy)" stroke-width="1.8"/></svg>Eligibility</h3><p>Lorem Ipsum is simply dummy text of the printing been</p></li>
      <li><h3><svg width="12" height="12" viewBox="0 0 12 12"><rect x=".5" y=".5" width="11" height="11" fill="none" stroke="var(--navy)"/><path d="M2.5 6l2.5 2.5 5-6" fill="none" stroke="var(--navy)" stroke-width="1.8"/></svg>Winners &amp; Prizes</h3><p>Lorem Ipsum is simply dummy text of the printing been</p></li>
      <li><h3><svg width="12" height="12" viewBox="0 0 12 12"><rect x=".5" y=".5" width="11" height="11" fill="none" stroke="var(--navy)"/><path d="M2.5 6l2.5 2.5 5-6" fill="none" stroke="var(--navy)" stroke-width="1.8"/></svg>Privacy Policy</h3><p>Lorem Ipsum is simply dummy text of the printing been</p></li>
      <li><h3><svg width="12" height="12" viewBox="0 0 12 12"><rect x=".5" y=".5" width="11" height="11" fill="none" stroke="var(--navy)"/><path d="M2.5 6l2.5 2.5 5-6" fill="none" stroke="var(--navy)" stroke-width="1.8"/></svg>Judging</h3><p>Lorem Ipsum is simply dummy text of the printing been</p></li>
      <li><h3><svg width="12" height="12" viewBox="0 0 12 12"><rect x=".5" y=".5" width="11" height="11" fill="none" stroke="var(--navy)"/><path d="M2.5 6l2.5 2.5 5-6" fill="none" stroke="var(--navy)" stroke-width="1.8"/></svg>Disclaimer</h3><p>Lorem Ipsum is simply dummy text of the printing been</p></li>
    </ul>
  </div>
</section>

<section class="blog">
  <h2 class="section-title">Our Blog</h2>
  <p class="section-sub">Lorem Ipsum is simply dummy text of the</p>
  <div class="posts">
    <article class="post"><div class="photo p1" role="img" aria-label="Woman with long hair in a light coat"></div>
      <div class="body"><h3>Introduction</h3><time>7 - Feb - 2017</time><p>Lorem Ipsum is simply dummy text of the printing and typesetting industry. Lorem Ipsum has been the industry's standard dummy text ever since the 1500s, when an unknown printer.</p><a class="btn" href="#">Read More</a></div></article>
    <article class="post"><div class="photo p2" role="img" aria-label="Woman in sunglasses wearing a dark jacket"></div>
      <div class="body"><h3>Introduction</h3><time>7 - Feb - 2017</time><p>Lorem Ipsum is simply dummy text of the printing and typesetting industry. Lorem Ipsum has been the industry's standard dummy text ever since the 1500s, when an unknown printer.</p><a class="btn" href="#">Read More</a></div></article>
    <article class="post"><div class="photo p3" role="img" aria-label="Woman in black outfit walking past a stone staircase"></div>
      <div class="body"><h3>Introduction</h3><time>7 - Feb - 2017</time><p>Lorem Ipsum is simply dummy text of the printing and typesetting industry. Lorem Ipsum has been the industry's standard dummy text ever since the 1500s, when an unknown printer.</p><a class="btn" href="#">Read More</a></div></article>
  </div>
</section>

<footer class="site-footer">
  <a class="btn signup" href="#">Sign Up</a>
  <small>© 2009 - 2017 vendrow.com</small>
  <nav class="footer-nav"><a href="#">Home</a><a href="#">Forum</a><a href="#">Standings</a><a href="#">FAQ</a><a href="#">Blog</a><a href="#">Contact</a></nav>
</footer>

</body>
</html>
```